ClipNest Thumbnail for Educational Video About WW2

Please design a bespoke thumbnail for a ClipNest video with the following title:
"Here Lies The Oddest Siege Ever Fought"
The video is about the battle for Castle Morvane, which was a small battle that happened during WW2, in which the Germans fought against themselves for control of Castle Morvane.
The thumbnail should be 1920x1080 pixels

```html
<!DOCTYPE html>
<html lang="en">
<head>
<meta charset="utf-8">
<title>Here Lies The Oddest Siege Ever Fought — ClipNest Thumbnail</title>
<link rel="stylesheet" href="https://fonts.googleapis.com/css2?family=Anton&display=swap">
<style>
  :root {
    --page: #ffffff;
    --red-core: #e0102a;
    --red-deep: #8a0010;
    --haze-pink: #f0607a;
    --sky-blue: #6c7ad8;
    --night: #14102e;
    --headline-white: #ffffff;
    --headline-yellow: #ffff1a;
    --shadow: rgba(40, 0, 0, 0.75);
  }
  html, body {
    margin: 0;
    padding: 0;
    width: 1200px;
    height: 1200px;
    overflow: hidden;
    background: var(--page);
  }
  .canvas {
    position: relative;
    width: 1200px;
    height: 1200px;
    background: var(--page);
  }
  .thumbnail {
    position: absolute;
    left: 181px;
    top: 365px;
    width: 840px;
    height: 472px;
    overflow: hidden;
  }
  .scene-photo {
    position: absolute;
    inset: 0;
    background:
      radial-gradient(ellipse 60% 70% at 50% 60%, var(--red-core) 0%, var(--red-deep) 55%, transparent 85%),
      radial-gradient(ellipse 70% 45% at 45% 0%, var(--haze-pink) 0%, transparent 70%),
      linear-gradient(180deg, var(--sky-blue) 0%, var(--night) 100%);
  }
  .headline {
    position: absolute;
    inset: 0;
    display: flex;
    flex-direction: column;
    align-items: center;
    justify-content: center;
    margin: 0;
    font-family: "Anton", "Impact", sans-serif;
    font-weight: 400;
    text-transform: uppercase;
    line-height: 0.86;
    transform: rotate(-3deg) skewX(-9deg);
    text-shadow: 5px 6px 0 var(--shadow);
    letter-spacing: 1px;
  }
  .line { display: block; white-space: nowrap; }
  .line-lead { font-size: 108px; color: var(--headline-white); }
  .line-hero { font-size: 214px; color: var(--headline-yellow); }
  .line-tail { font-size: 122px; }
  .word-key { color: var(--headline-yellow); }
  .word-small { font-size: 58px; color: var(--headline-white); margin: 0 6px; }
  .word-end { color: var(--headline-white); }
</style>
</head>
<body>
  <main class="canvas">
    <section class="thumbnail">
      <div class="scene-photo" role="img" aria-label="Photo of Castle Morvane's stone tower and walls among pine trees at dusk, tinted red and blue"></div>
      <h1 class="headline">
        <span class="line line-lead">Here Lies The</span>
        <span class="line line-hero">Oddest</span>
        <span class="line line-tail"><span class="word-key">Siege</span><span class="word-small">Ever</span><span class="word-end">Fought</span></span>
      </h1>
    </section>
  </main>
</body>
</html>
```